Business Card Design - Law Firm

We are a boutique law firm located near the beach in Manly, Australia. We have recently had a new logo designed and are revamping our business cards with the new logo.

We have recently had a business card design done for us but are not entirely happy with it. We are looking for something modern, simplistic but striking. We would like to see multiple designs.

We have attached a word document which includes our new logo and the current business card design which we are looking at moving away from.

We would like the business cards to be double sided. We would like the design to include something which we can print in gloss colour when we send it to the business card printers.

```html
<!DOCTYPE html>
<html lang="en">
<head>
<meta charset="UTF-8">
<title>Harbord &amp; Partners Lawyers – Business Card</title>
<link rel="stylesheet" href="https://fonts.googleapis.com/css2?family=Montserrat:wght@400;500;600;700&display=swap">
<style>
  :root {
    --backdrop: #2b2b2d;
    --navy: #2e3b8a;
    --navy-mid: #4a5ba6;
    --periwinkle: #7189c8;
    --ink: #222226;
    --paper: #ffffff;
    --white: #ffffff;
  }
  * { box-sizing: border-box; margin: 0; padding: 0; }
  html, body {
    width: 1200px; height: 1200px; overflow: hidden;
    background: var(--backdrop);
    font-family: "Montserrat", sans-serif;
  }
  .sheet {
    width: 1200px; height: 1200px;
    display: flex; flex-direction: column; align-items: center; justify-content: center;
    gap: 44px;
  }
  .card {
    position: relative;
    width: 900px; height: 514px;
    border-radius: 4px;
    overflow: hidden;
    box-shadow: 0 12px 30px rgba(0,0,0,.45);
  }

  /* Reverse side */
  .card-back {
    background:
      radial-gradient(ellipse 60% 45% at 30% 30%, rgba(255,255,255,.08), transparent 70%),
      radial-gradient(ellipse 55% 40% at 75% 72%, rgba(255,255,255,.07), transparent 70%),
      linear-gradient(90deg, var(--navy) 0%, var(--navy) 35%, var(--navy-mid) 70%, var(--periwinkle) 100%);
  }
  .card-back .backdrop-art {
    position: absolute; inset: 0;
  }
  .back-wordmark {
    position: absolute; left: 0; right: 0; top: 205px;
    text-align: center; color: var(--white);
  }
  .back-wordmark .firm-name {
    font-size: 38px; font-weight: 600; letter-spacing: 4px;
  }
  .back-wordmark .firm-type {
    margin-top: 10px;
    font-size: 20px; font-weight: 600; letter-spacing: 18px;
  }

  /* Front side */
  .card-front { background: var(--paper); }
  .front-wave { position: absolute; inset: 0; }
  .front-wordmark {
    position: absolute; left: 70px; top: 92px;
    color: var(--ink);
    display: flex; align-items: center; gap: 16px;
  }
  .front-wordmark .mark-dot {
    width: 22px; height: 22px; border-radius: 50%;
    background: var(--navy);
  }
  .front-wordmark .firm-name {
    font-size: 30px; font-weight: 700; letter-spacing: 2px; line-height: 1.3;
  }
  .front-wordmark .firm-type {
    display: block;
    font-size: 17px; font-weight: 700; letter-spacing: 14px;
  }

  .contact {
    position: absolute; right: 60px; bottom: 46px;
    text-align: right; color: var(--ink);
  }
  .contact .person-name {
    font-size: 34px; font-weight: 700; color: var(--navy-mid); letter-spacing: .5px;
  }
  .contact .person-role {
    font-size: 20px; font-weight: 500; margin-top: 2px; margin-bottom: 18px;
  }
  .contact .detail {
    display: flex; justify-content: flex-end; align-items: center; gap: 12px;
    font-size: 18px; font-weight: 500; line-height: 1.55;
  }
  .contact .detail svg { width: 18px; height: 18px; flex: none; }
  .contact .detail.address { padding-right: 30px; }
</style>
</head>
<body>
<main class="sheet">

  <section class="card card-back" aria-label="Card reverse">
    <svg class="backdrop-art" viewBox="0 0 900 514" preserveAspectRatio="none" aria-hidden="true">
      <path d="M0,320 C200,260 420,250 620,300 S850,380 900,360 L900,420 C800,440 640,360 460,340 S150,340 0,400 Z" fill="rgba(255,255,255,.06)"/>
    </svg>
    <div class="back-wordmark">
      <div class="firm-name">Harbord &amp; Partners</div>
      <div class="firm-type">LAWYERS</div>
    </div>
  </section>

  <section class="card card-front" aria-label="Card front">
    <svg class="front-wave" viewBox="0 0 900 514" preserveAspectRatio="none" aria-hidden="true">
      <defs>
        <linearGradient id="band-fill" x1="0" x2="1" y1="0" y2="0">
          <stop offset="0" stop-color="#2e3b8a"/>
          <stop offset=".55" stop-color="#33439a"/>
          <stop offset="1" stop-color="#7189c8"/>
        </linearGradient>
      </defs>
      <path d="M0,300 C120,350 260,360 420,300 S720,150 900,135
               L900,235 C780,205 640,220 500,280 S160,410 0,345 Z"
            fill="url(#band-fill)"/>
    </svg>

    <div class="front-wordmark">
      <span class="mark-dot" aria-hidden="true"></span>
      <div class="firm-name">Harbord &amp; Partners<span class="firm-type">LAWYERS</span></div>
    </div>

    <div class="contact">
      <div class="person-name">Maya Ellison</div>
      <div class="person-role">Practice Manager</div>
      <div class="detail">(02) 9000 4815
        <svg viewBox="0 0 24 24" aria-label="Phone"><path fill="#3c4ea3" d="M6.6 10.8a15.1 15.1 0 0 0 6.6 6.6l2.2-2.2c.3-.3.7-.4 1-.2 1.1.4 2.3.6 3.6.6.6 0 1 .4 1 1V20c0 .6-.4 1-1 1A17 17 0 0 1 3 4c0-.6.4-1 1-1h3.5c.6 0 1 .4 1 1 0 1.3.2 2.5.6 3.6.1.3 0 .7-.2 1z"/></svg>
      </div>
      <div class="detail">maya.ellison@northbeachlaw.com.au
        <svg viewBox="0 0 24 24" aria-label="Email"><rect x="2" y="5" width="20" height="14" rx="1.5" fill="#3c4ea3"/><path d="M3 6l9 7 9-7" stroke="#fff" stroke-width="1.6" fill="none"/></svg>
      </div>
      <div class="detail">www.harbordpartners.com.au
        <svg viewBox="0 0 24 24" aria-label="Website"><circle cx="12" cy="12" r="9.5" fill="none" stroke="#3c4ea3" stroke-width="2"/><ellipse cx="12" cy="12" rx="4" ry="9.5" fill="none" stroke="#3c4ea3" stroke-width="1.6"/><path d="M2.5 12h19M4 7h16M4 17h16" stroke="#3c4ea3" stroke-width="1.4"/></svg>
      </div>
      <div class="detail address">Suite 4, 12 Coral Lane, SEAVIEW NSW 2100</div>
    </div>
  </section>

</main>
</body>
</html>
```